Velmoro Consulting Business

** Please add the content information from my old business card
1. I would like to see a two sided business card with both options with the 1st Option--Sketch Nest-new WHITE BACKGROUND LOGO
2 nd Option-Sketch Nest - new BLACK- Background Logo
3rd -Option a business card with my Photo on the card
Please add the new word to the card information:
EXECUTION
AS THE OWNER'S REP
WE AIM TO ACHIEVE YOUR
INFRASTRUCTURE VISION with
OUR SPECIALIZATION & EXECUTION in:

FUNDING Planning
BUSINESS Planning
INFRASTRUCTURE Planning
PROJECT Management
Since 2012
_____________________________________________________________________
I want to get spot uv raised printing. I was liking a a nice rich white linen paper stock with black writing & NOT A COLORED CARD other than a variety of white or black cards concept

```html
<!DOCTYPE html>
<html lang="en">
<head>
<meta charset="utf-8">
<title>Velmoro Consulting – Business Card</title>
<link href="https://fonts.googleapis.com/css2?family=Arimo:wght@400;700&display=swap" rel="stylesheet">
<style>
  :root {
    --page: #1c1c1d;
    --card-white: #f4f4f4;
    --card-dark: #2a2a2c;
    --ink: #222224;
    --red: #d8213a;
    --white: #ffffff;
    --faint: #3b3b3e;
  }
  * { margin: 0; padding: 0; box-sizing: border-box; }
  html, body {
    width: 1200px; height: 1059px; overflow: hidden;
    background: var(--page);
    font-family: "Arimo", Arial, sans-serif;
  }
  .card {
    position: absolute;
    width: 690px; height: 392px;
    border-radius: 22px;
    overflow: hidden;
  }
  .card-front { left: 255px; top: 89px; background: var(--card-white); }
  .card-back  { left: 255px; top: 547px; background: var(--card-dark); }

  /* front */
  .brand {
    position: absolute; left: 60px; top: 160px; width: 230px;
    display: flex; align-items: center; gap: 10px;
  }
  .brand-mark { width: 18px; height: 18px; background: var(--red); flex: none; }
  .brand-name { font-weight: 700; font-size: 25px; color: var(--ink); line-height: 1.1; }
  .divider {
    position: absolute; left: 306px; top: 122px; width: 1.5px; height: 146px;
    background: var(--ink);
  }
  .person { position: absolute; left: 333px; top: 116px; }
  .person-name { font-weight: 700; font-size: 25px; color: var(--red); }
  .person-title { font-size: 16px; color: var(--ink); margin-top: 6px; letter-spacing: .2px; }
  .contacts { position: absolute; left: 333px; top: 197px; list-style: none; }
  .contacts li {
    display: flex; align-items: center; gap: 8px;
    font-size: 17px; color: var(--ink); height: 25.5px;
  }
  .contacts svg { width: 13px; height: 13px; flex: none; }
  .wave { position: absolute; left: 0; bottom: 0; width: 690px; height: 70px; }
  .locations {
    position: absolute; right: 28px; bottom: 13px;
    font-size: 16px; color: var(--white);
  }

  /* back */
  .back-brand {
    position: absolute; left: 0; right: 0; top: 55px; text-align: center;
    font-weight: 700; font-size: 50px; color: var(--faint); letter-spacing: 1px;
  }
  .statement {
    position: absolute; left: 0; right: 0; top: 164px; text-align: center;
    font-size: 19px; line-height: 30px; color: var(--white);
  }
  .statement .lead { color: var(--red); }
  .rule { position: absolute; left: 0; right: 0; height: 1.5px; background: var(--red); }
  .rule-top { top: 258px; }
  .rule-bottom { top: 354px; }
  .services {
    position: absolute; left: 0; right: 0; top: 272px; text-align: center;
    font-size: 18px; line-height: 32px; color: var(--white);
  }
  .services .sep { color: var(--red); margin: 0 6px; }
  .since {
    position: absolute; left: 50%; top: 342px; transform: translateX(-50%);
    padding: 2px 10px; border: 1.5px solid var(--red); border-radius: 14px;
    background: var(--card-dark); color: var(--white); font-size: 18px;
  }
</style>
</head>
<body>

<section class="card card-front">
  <div class="brand">
    <span class="brand-mark"></span>
    <span class="brand-name">Velmoro Consulting</span>
  </div>
  <div class="divider"></div>
  <div class="person">
    <p class="person-name">Marisol Trent-Okafor</p>
    <p class="person-title">CEO / LEAD PROJECT MANAGER</p>
  </div>
  <ul class="contacts">
    <li>
      <svg viewBox="0 0 16 16"><path fill="#d8213a" d="M2 6c0-2 3-3 6-3s6 1 6 3v1h-3V6H5v1H2zM4 8h8l2 5H2z"/></svg>
      555.301.7742
    </li>
    <li>
      <svg viewBox="0 0 16 16"><path fill="#d8213a" d="M1 6l7-5 7 5v9H1z"/><path fill="none" stroke="#fff" stroke-width="1" d="M1 6l7 5 7-5"/></svg>
      mara@velmoro.ca
    </li>
    <li>
      <svg viewBox="0 0 16 16"><circle cx="8" cy="8" r="7" fill="#d8213a"/><path fill="none" stroke="#fff" stroke-width="1" d="M1 8h14M8 1c-3 3-3 11 0 14M8 1c3 3 3 11 0 14"/></svg>
      www.velmoro.ca
    </li>
  </ul>
  <svg class="wave" viewBox="0 0 690 70" preserveAspectRatio="none" aria-hidden="true">
    <path fill="#2a2a2c" d="M0 4 C120 60 250 50 420 32 C560 16 640 6 690 35 L690 70 L0 70 Z"/>
    <path fill="#d8213a" d="M15 8 C140 60 260 48 420 30 C560 14 640 2 690 22 L690 35 C640 6 560 16 420 32 C250 50 120 60 15 8 Z"/>
  </svg>
  <p class="locations">Harrowgate NT • Belcourt NB</p>
</section>

<section class="card card-back">
  <p class="back-brand">Velmoro Consulting</p>
  <div class="statement">
    <p class="lead">AS THE OWNER'S REP</p>
    <p>WE AIM TO ACHIEVE YOUR INFRASTRUCTURE VISION</p>
    <p>with OUR SPECIALIZATION &amp; EXECUTION in:</p>
  </div>
  <div class="rule rule-top"></div>
  <div class="services">
    <p>FUNDING Planning<span class="sep">|</span>BUSINESS Planning</p>
    <p>INFRASTRUCTURE Planning<span class="sep">|</span>PROJECT Management</p>
  </div>
  <div class="rule rule-bottom"></div>
  <p class="since">Since 2012</p>
</section>

</body>
</html>
```